Hollowbrook Yard Services - Needs a business card! Easy JOB!

I need a business card for a new company called Hollowbrook Yard Services. I will be offering the below services.

I am relatively open for ideas, so please be at your creative best.

I think I will list all the services offered on the rear of the card.

- Gardening
- Lawn Care
- Hedge Trimming
- Rubbish Removal
- Weeding/Spraying
- Landscaping
- Gutter Cleaning
- Solar Panel Cleaning
- Irrigation
- Pruning
- On-Site Mulching
- Ask for other services

I am still a little undecided on the colours. I prefer the logos with the Blue text, but I am open for ideas ( the logo/texts colours are not final).

Please use the catch phrase "What can Hollowbrook do for you?"

Here are the required details.

Hollowbrook Yard Services

Miles Fenwarick (owner)
Ph: 1300 555 014
Mob: 0400 555 286

miles@hollowbrookyard.com.au
www.hollowbrookyard.com.au
chatterly.com/HollowbrookYard
quipster.com/HollowbrookYard
ABN: 555 019 472 ( this can be in smaller text somewhere, this is the least important )

Thankyou in advance! And good luck.

regards,
Miles
Updates

Hi everyone, please make sure you include the phrase "What can Hollowbrook do for you?" on the designs.

thanks,
Miles

Definitely liking the focus on a majority of the design on the blue colour from the logo. Also a splash of green in the plant.

Please make sure you list the services provided on the rear of the card. thanks.

With the service listing, please make "ask for other services" stand out, either a different colour or position or size... as long as it is more noticeable than the other services listed. Thanks.

Industry/Entity Type

Business

Requirements
Must have
• - use the font supplied (Brandon Family Font)
- use of the catch phrase "What can Hollowbrook do for you?"
- Double sided design
- Chatterly and Quipster logos/links
- Please use symbol/picture for "phone" "mobile" "email" instead of using the words.
- List the services provided on the rear of the card

```html
<!DOCTYPE html>
<html lang="en">
<head>
<meta charset="utf-8">
<title>Hollowbrook Yard Services – Business Card</title>
<link rel="stylesheet" href="https://fonts.googleapis.com/css2?family=Jost:wght@300;400;500;600;700&display=swap">
<style>
  :root {
    --page-bg: #e9e7e3;
    --card-white: #ffffff;
    --card-dark: #3b3c3f;
    --brand-blue: #1e46b4;
    --band-blue-deep: #1a2f95;
    --band-blue-bright: #2d5fd8;
    --band-edge: #6f8ff0;
    --bullet-blue: #2f8fe6;
    --ink: #2a2a2c;
    --ink-soft: #555659;
    --rule: #cfd0d2;
    --leaf-green: #5aa83c;
    --white: #ffffff;
  }
  * { box-sizing: border-box; margin: 0; padding: 0; }
  html, body {
    width: 1200px; height: 900px; overflow: hidden;
    background: var(--page-bg);
    font-family: "Jost", sans-serif;
    color: var(--ink);
  }
  .sheet {
    width: 1200px; height: 900px;
    display: flex; flex-direction: column;
    align-items: center; justify-content: center; gap: 40px;
  }
  .card {
    width: 640px; height: 391px;
    position: relative; overflow: hidden;
    box-shadow: 0 6px 18px rgba(0,0,0,.18);
  }

  /* ---------- Front ---------- */
  .card--front { background: var(--card-white); display: flex; }
  .brand {
    width: 300px; display: flex; align-items: center; justify-content: center;
  }
  .brand__lockup { display: flex; align-items: center; gap: 12px; }
  .brand__dot {
    width: 22px; height: 22px; border-radius: 50%;
    background: var(--leaf-green); flex: none;
  }
  .brand__name {
    font-weight: 700; font-size: 30px; line-height: 1.05;
    color: var(--brand-blue); letter-spacing: .5px;
  }
  .divider {
    width: 1px; background: var(--rule);
    margin: 56px 0;
  }
  .contact {
    flex: 1; padding: 58px 0 0 34px;
    display: flex; flex-direction: column;
  }
  .contact__name { font-size: 19px; font-weight: 600; }
  .contact__role { font-weight: 400; color: var(--ink-soft); }
  .line {
    display: flex; align-items: center; gap: 8px;
  }
  .line svg { width: 12px; height: 12px; flex: none; fill: var(--brand-blue); }
  .phones { margin-top: 6px; font-size: 19px; font-weight: 400; line-height: 1.45; }
  .online {
    margin-top: 34px; font-size: 14px; font-weight: 400; line-height: 1.6;
  }
  .social-mark { width: 11px; height: 11px; background: var(--brand-blue); flex: none; margin: 0 1px; }
  .abn { padding-left: 20px; }

  /* ---------- Back ---------- */
  .card--back { background: var(--card-dark); color: var(--white); }
  .tagline-band {
    height: 74px; margin-top: 24px;
    background: linear-gradient(90deg, var(--band-blue-deep), var(--band-blue-bright));
    border-top: 3px solid var(--band-edge);
    display: flex; align-items: center; justify-content: center;
  }
  .tagline {
    font-size: 34px; font-weight: 500; letter-spacing: .3px;
  }
  .services {
    display: grid; grid-template-columns: 1fr 1fr;
    padding: 28px 50px 0 70px; column-gap: 30px;
  }
  .services__list { list-style: none; font-size: 21px; font-weight: 300; line-height: 1.6; }
  .services__list li { display: flex; align-items: center; gap: 12px; white-space: nowrap; }
  .services__list li::before {
    content: ""; width: 0; height: 0;
    border-left: 8px solid var(--bullet-blue);
    border-top: 5px solid transparent; border-bottom: 5px solid transparent;
  }
  .services__list .service--highlight {
    font-weight: 600; font-size: 22px; color: var(--bullet-blue);
  }
</style>
</head>
<body>
<main class="sheet">

  <section class="card card--front" aria-label="Business card front">
    <div class="brand">
      <div class="brand__lockup">
        <span class="brand__dot"></span>
        <span class="brand__name">Hollowbrook<br>Yard Services</span>
      </div>
    </div>
    <div class="divider"></div>
    <div class="contact">
      <p class="contact__name">Miles Fenwarick <span class="contact__role">owner</span></p>
      <div class="phones">
        <p class="line">
          <svg viewBox="0 0 24 24" aria-label="Phone"><path d="M6.6 10.8a15 15 0 0 0 6.6 6.6l2.2-2.2a1 1 0 0 1 1-.25 11.4 11.4 0 0 0 3.6.6 1 1 0 0 1 1 1V20a1 1 0 0 1-1 1A17 17 0 0 1 3 4a1 1 0 0 1 1-1h3.5a1 1 0 0 1 1 1c0 1.25.2 2.45.6 3.6a1 1 0 0 1-.25 1z"/></svg>
          1300 555 014
        </p>
        <p class="line">
          <svg viewBox="0 0 24 24" aria-label="Mobile"><path d="M7 1h10a2 2 0 0 1 2 2v18a2 2 0 0 1-2 2H7a2 2 0 0 1-2-2V3a2 2 0 0 1 2-2zm0 3v14h10V4zm5 15.5a1.2 1.2 0 1 0 0 2.4 1.2 1.2 0 0 0 0-2.4z"/></svg>
          0400 555 286
        </p>
      </div>
      <div class="online">
        <p class="line">
          <svg viewBox="0 0 24 24" aria-label="Email"><path d="M2 5h20v14H2zm2 2v.5l8 5 8-5V7zm0 3v7h16v-7l-8 5z"/></svg>
          miles@hollowbrookyard.com.au
        </p>
        <p class="line">
          <svg viewBox="0 0 24 24" aria-label="Website"><path d="M12 2a10 10 0 1 0 0 20 10 10 0 0 0 0-20zm6.9 6h-3a15 15 0 0 0-1.3-3.9A8 8 0 0 1 18.9 8zM12 4c.8 1.1 1.5 2.5 1.9 4h-3.8c.4-1.5 1.1-2.9 1.9-4zM4.3 14a8 8 0 0 1 0-4h3.4a16 16 0 0 0 0 4zm.8 2h3a15 15 0 0 0 1.3 3.9A8 8 0 0 1 5.1 16zm3-8h-3a8 8 0 0 1 4.3-3.9A15 15 0 0 0 8.1 8zM12 20c-.8-1.1-1.5-2.5-1.9-4h3.8c-.4 1.5-1.1 2.9-1.9 4zm2.3-6H9.7a14 14 0 0 1 0-4h4.6a14 14 0 0 1 0 4zm.3 5.9a15 15 0 0 0 1.3-3.9h3a8 8 0 0 1-4.3 3.9zm1.7-5.9a16 16 0 0 0 0-4h3.4a8 8 0 0 1 0 4z"/></svg>
          www.hollowbrookyard.com.au
        </p>
        <p class="line"><span class="social-mark"></span>chatterly.com/HollowbrookYard</p>
        <p class="line"><span class="social-mark"></span>quipster.com/HollowbrookYard</p>
        <p class="abn">ABN: 555 019 472</p>
      </div>
    </div>
  </section>

  <section class="card card--back" aria-label="Business card back">
    <div class="tagline-band">
      <h1 class="tagline">What can Hollowbrook do for you?</h1>
    </div>
    <div class="services">
      <ul class="services__list">
        <li>Gardening</li>
        <li>Lawn Care</li>
        <li>Hedge Trimming</li>
        <li>Rubbish Removal</li>
        <li>Weeding/Spraying</li>
        <li>Landscaping</li>
      </ul>
      <ul class="services__list">
        <li>Gutter Cleaning</li>
        <li>Solar Panel Cleaning</li>
        <li>Irrigation</li>
        <li>Pruning</li>
        <li>On-Site Mulching</li>
        <li class="service--highlight">Ask for other services</li>
      </ul>
    </div>
  </section>

</main>
</body>
</html>
```